Corp Deck - Kestrel Lane Nursing

Kestrel Lane Nursing is a home health care company based in Ontario, Canada. The company's core belief is that homecare should be the foundational element of healthcare, and that a significant change needs to happen in how healthcare is delivered. We call this “Wholehearted Wellness Indoors”.

Kestrel Lane Nursing helps people deal with chronic conditions, ageing, and medical recovery in their home. We ensure a unified, complete experience all the way from matching the optimal care and caregiver with the client, to being a trusted navigator, helping the client and their family deal with the complex healthcare system.

This wholehearted wellness indoors is not only less stressful, but also drives better health outcomes.

We have been working on updating the content of our corporate deck to align with our new brand design. In addition to incorporating our new brand elements, we would like to introduce new templates, including our updated colors (along with complementary ones), graphics, and more suitable fonts. There are 21 slides.

Target Market(s)

For this corporate deck, the target audience consists of potential investors, industry leaders, and recognized media figures who possess a solid understanding of the industry and are keen to learn more about our wholehearted wellness indoors. These individuals are well-versed in the industry and expect presentations that stand out and capture their attention effectively. They typically have a high level of education.

Industry/Entity Type

Healthcare

Requirements
Must have
• Align the design with the new company's branding (see it on our website www.kestrellanenursing.example) emphasizing the vision of home care as the foundation of healthcare. Utilize a clean, modern design aesthetic that communicates trustworthiness, empathy, and professionalism. Incorporate the company's branding color palette and supplement it with hues that evoke feelings of trust, comfort, and reliability.
Nice to have
• Shapes, graphics, images that capture the essence of our wholehearted wellness indoors. Emphasize the human aspect of home health care.
Should not have
• Shapes, graphics, images, that infantilize older people or disrespect their dignity.

```html
<!DOCTYPE html>
<html lang="en">
<head>
<meta charset="utf-8">
<title>Kestrel Lane Nursing – Corporate Deck</title>
<link href="https://fonts.googleapis.com/css2?family=Open+Sans:wght@400;600;700;800&display=swap" rel="stylesheet">
<style>
:root{
  --purple:#5b2383;
  --purple-mid:#7a4a9e;
  --purple-light:#b89ccc;
  --green:#6cc04a;
  --ink:#1b1b1b;
  --text:#333;
  --paper:#ffffff;
  --map-red:#e31b3f;
}
*{margin:0;padding:0;box-sizing:border-box}
html,body{width:687px;height:1200px;overflow:hidden;background:var(--paper)}
body{position:relative;font-family:"Open Sans",Arial,sans-serif;color:var(--text)}
.slide{position:absolute;overflow:hidden;background:var(--paper);box-shadow:0 2px 6px rgba(0,0,0,.18)}
.hero{left:24px;top:25px;width:639px;height:359px;background:var(--purple)}
.col-l{left:24px;width:309px;height:174px}
.col-r{left:354px;width:309px;height:174px}
.row1{top:408px}.row2{top:606px}.row3{top:804px}.row4{top:1001px}
.abs{position:absolute}
.brand-chip{position:absolute;left:8px;bottom:7px;height:12px;padding:0 4px;background:var(--purple);color:#fff;font-size:4.3px;font-weight:700;line-height:12px;letter-spacing:.2px;display:flex;align-items:center;gap:2px}
.brand-chip i{display:inline-block;width:4px;height:4px;background:var(--green)}
.page-no{position:absolute;right:8px;bottom:8px;width:10px;height:10px;border:1px solid var(--purple);border-radius:50%;font-size:4.5px;font-weight:700;color:var(--purple);display:flex;align-items:center;justify-content:center;background:#fff}
.hero-photo{position:absolute;right:0;top:0;width:330px;height:359px;background:linear-gradient(160deg,#b8cf8a 0%,#d9d3e6 35%,#f3eef6 55%,#8fae5c 100%)}
.hero-fade{position:absolute;right:180px;top:0;width:160px;height:359px;background:linear-gradient(90deg,var(--purple),rgba(91,35,131,0))}
.hero-brand{position:absolute;left:56px;top:110px;color:#fff;font-size:17px;font-weight:800;display:flex;align-items:center;gap:7px;letter-spacing:.3px}
.hero-brand i{width:14px;height:14px;border-radius:50%;background:var(--green)}
.hero-title{position:absolute;left:54px;top:158px;color:#fff;font-size:31px;font-weight:800;line-height:40px}
.split-title{color:#fff;font-size:13px;font-weight:800;line-height:16px}
.center-title{position:absolute;left:0;right:0;text-align:center;font-weight:800;color:var(--ink)}
.center-title .accent,.left-title .accent{color:var(--green)}
.center-title .dark{color:var(--purple)}
.rule{position:absolute;height:1px;background:var(--purple)}
.driver{position:absolute;width:145px;font-size:4.6px;line-height:5.6px;color:var(--text)}
.driver h4{font-size:4.8px;font-weight:700;color:var(--ink);margin-bottom:2px}
.driver ul{padding-left:8px}
.driver svg{display:block;margin:0 0 5px 26px}
.left-title{position:absolute;left:21px;top:13px;font-size:13px;font-weight:800;color:var(--ink)}
.list-item{position:absolute;left:21px;display:flex;align-items:center;gap:7px;font-size:4.8px;line-height:7.5px;color:var(--ink);width:170px}
.num{flex:none;width:10px;height:10px;border-radius:50%;background:var(--purple);color:#fff;font-size:4.5px;font-weight:700;display:flex;align-items:center;justify-content:center}
.diag-panel{position:absolute;inset:0}
.photo{position:absolute}
.callout{position:absolute;left:25px;top:44px;width:260px;height:42px;background:var(--purple);color:#fff;font-size:4.7px;line-height:5.4px;text-align:center;display:flex;align-items:center;justify-content:center;padding:0 28px}
.small-list{position:absolute;left:31px;font-size:4.8px;color:var(--ink);display:flex;align-items:center;gap:5px}
.small-list .num{width:9px;height:9px}
.note{position:absolute;font-size:2.8px;line-height:3.4px;color:#555}
</style>
</head>
<body>

<!-- Cover -->
<section class="slide hero">
  <div class="hero-photo" role="img" aria-label="Photo of a smiling caregiver with her hands on the shoulders of an older woman in a wheelchair, in a sunny park"></div>
  <div class="hero-fade"></div>
  <div class="hero-brand"><i></i>KESTREL LANE NURSING</div>
  <h1 class="hero-title">Wholehearted<br>Wellness<br>Indoors</h1>
</section>

<!-- 01 Question -->
<section class="slide col-l row1" style="background:var(--purple)">
  <svg class="diag-panel" width="309" height="174" viewBox="0 0 309 174"><polygon points="309,0 309,174 50,174" fill="var(--green)"/></svg>
  <h2 class="abs split-title" style="left:23px;top:30px">Is the Home Healthcare<br>model broken?</h2>
  <div class="abs" style="left:143px;top:68px;color:#fff;font-size:40px;font-weight:600">?</div>
  <div class="abs" style="left:207px;top:93px;color:#fff;font-size:30px;font-weight:800">No,</div>
  <p class="abs" style="left:168px;top:130px;color:#fff;font-size:8.2px;line-height:10px">because the model has never been<br>accurately defined, or described.</p>
  <div class="brand-chip"><i></i>KESTREL LANE NURSING</div>
  <div class="page-no">01</div>
</section>

<!-- 02 Pie -->
<section class="slide col-r row1">
  <svg class="abs" style="left:0;top:0" width="309" height="174" viewBox="0 0 309 174" font-family="Open Sans, sans-serif" font-size="3.8" fill="#333">
    <g stroke="#fff" stroke-width=".5">
      <path d="M165 95 L165 38 A57 57 0 0 1 213.1 125.5Z" fill="#5b2383"/>
      <path d="M165 95 L213.1 125.5 A57 57 0 0 1 140.7 146.6Z" fill="#6a3292"/>
      <path d="M165 95 L140.7 146.6 A57 57 0 0 1 109 105.7Z" fill="#7a4a9e"/>
      <path d="M165 95 L109 105.7 A57 57 0 0 1 110.8 77.4Z" fill="#8a5eab"/>
      <path d="M165 95 L110.8 77.4 A57 57 0 0 1 123.4 56Z" fill="#9874b6"/>
      <path d="M165 95 L123.4 56 A57 57 0 0 1 144 42Z" fill="#a888c2"/>
      <path d="M165 95 L144 42 A57 57 0 0 1 154.3 39Z" fill="#b89ccc"/>
      <path d="M165 95 L154.3 39 A57 57 0 0 1 165 38Z" fill="#cbb6da"/>
    </g>
    <g fill="#fff" font-size="3.6"><text x="205" y="72">34%</text><text x="174" y="146">23%</text><text x="120" y="126">15%</text><text x="111" y="92">8%</text><text x="118" y="70">7%</text><text x="134" y="52">7%</text><text x="149" y="46">3%</text><text x="158" y="45">3%</text></g>
    <g stroke="var(--purple)" stroke-width=".6" fill="none">
      <polyline points="204,61 210,61 210,60 230,60"/>
      <polyline points="212,138 212,142 210,142"/>
      <polyline points="119,125 97,125"/>
      <polyline points="111,91 99,91"/>
      <polyline points="117,69 96,69"/>
      <polyline points="133,50 98,50"/>
      <polyline points="148,44 148,34 135,34"/>
      <polyline points="161,43 161,29 190,29"/>
    </g>
    <text x="231" y="62">Hospital</text><text x="231" y="66" font-weight="700">$25.8</text>
    <text x="212" y="144">OHIP(physician</text><text x="212" y="148">And practitioners</text><text x="212" y="152" font-weight="700">$17.0</text>
    <text x="66" y="126">Others program</text><text x="66" y="130" font-weight="700">$11.2</text>
    <text x="58" y="92">Long term care home</text><text x="58" y="96" font-weight="700">$5.6</text>
    <text x="40" y="74">Ontario public drug program</text><text x="40" y="78" font-weight="700">$5.4</text>
    <text x="54" y="50">Community program</text><text x="54" y="54" font-weight="700">$4.9</text>
    <text x="100" y="24">Mental health and</text><text x="100" y="28">addiction program</text><text x="100" y="32" font-weight="700">$2.2</text>
    <text x="190" y="28">Health capital</text><text x="190" y="32" font-weight="700">$2.0</text>
    <text x="122" y="166" font-size="2.6" fill="#555">Source: FAO analysis of information provided by the Ministry of Health 2021-2022 data</text>
  </svg>
  <div class="brand-chip"><i></i>KESTREL LANE NURSING</div>
  <div class="page-no">02</div>
</section>

<!-- 03 Drivers -->
<section class="slide col-l row2">
  <h2 class="center-title" style="top:13px;font-size:13px"><span class="dark">Key Industry </span><span class="accent">Drivers</span></h2>
  <div class="rule" style="left:142px;top:33px;width:25px"></div>
  <div class="driver" style="left:33px;top:38px">
    <svg width="12" height="16" viewBox="0 0 12 16" fill="var(--purple)"><circle cx="6" cy="2" r="2"/><path d="M4 5h4l1 5H7.5v6h-3v-6H3z"/><rect x="9.5" y="8" width=".8" height="8"/></svg>
    <h4>Rising Geriatric Population</h4>
    <ul><li>6.2 mill CDN's 65 and over will rise to 10.4 mill by 2037.</li><li>7 out of 10 will need long-term  care support.</li></ul>
  </div>
  <div class="driver" style="left:194px;top:38px">
    <svg width="14" height="16" viewBox="0 0 14 16" fill="none" stroke="var(--purple)" stroke-width="1.3"><circle cx="5" cy="2" r="1.4" fill="var(--purple)"/><path d="M5 5v5h5l2 4"/><path d="M3.5 8a4 4 0 1 0 6 4"/></svg>
    <h4>Increasing Chronic Conditions</h4>
    <ul><li>Notably dementia and Alzheimer's.</li><li>13.7% of CDN's have a disability.</li></ul>
  </div>
  <div class="driver" style="left:33px;top:92px">
    <svg width="10" height="16" viewBox="0 0 10 16" fill="none" stroke="var(--purple)" stroke-width="1.2"><rect x="1" y="1" width="8" height="14" rx="1.2"/><circle cx="5" cy="7" r="1.3"/><line x1="4" y1="13" x2="6" y2="13"/></svg>
    <h4>Digital Inflection Point</h4>
    <ul><li>HealthTech / Mobile</li><li>Back-end efficiencies</li><li>Behavioral: Less than 40% of CDN's have accessed HC records online.  But 4 out 5 CDN's want to use online HC resources..</li></ul>
  </div>
  <div class="driver" style="left:194px;top:92px">
    <svg width="16" height="16" viewBox="0 0 16 16" fill="var(--purple)" stroke="var(--purple)" stroke-width="1"><circle cx="8" cy="8" r="4.2"/><path d="M8 1v3M8 12v3M1 8h3M12 8h3M3 3l2 2M11 11l2 2M13 3l-2 2M5 11l-2 2"/></svg>
    <h4>Covid Reverberations and Change</h4>
    <ul><li>Covid impact still being felt.</li><li>Much change is permanent.</li></ul>
  </div>
  <div class="brand-chip"><i></i>KESTREL LANE NURSING</div>
  <div class="page-no">03</div>
</section>

<!-- 04 Bar chart -->
<section class="slide col-r row2">
  <h2 class="center-title" style="top:14px;font-size:8.4px">SPENDING ON <span class="accent">INSTITUTIONAL</span> CARE VS <span class="accent">HOME</span> CARE</h2>
  <div class="rule" style="left:142px;top:28px;width:25px"></div>
  <svg class="abs" style="left:56px;top:37px" width="200" height="108" viewBox="0 0 200 108" font-family="Open Sans, sans-serif">
    <rect x=".5" y=".5" width="199" height="107" fill="none" stroke="#ddd" stroke-width=".5"/>
    <g font-size="2.4" fill="#555" text-anchor="end">
      <text x="12" y="6">2.0</text><text x="12" y="13">1.8</text><text x="12" y="20">1.6</text><text x="12" y="26">1.4</text><text x="12" y="33">1.2</text><text x="12" y="40">1.0</text><text x="12" y="47">0.8</text><text x="12" y="53">0.6</text><text x="12" y="60">0.4</text><text x="12" y="67">0.2</text><text x="12" y="74">0.0</text>
    </g>
    <text x="5" y="50" font-size="2.8" fill="#444" transform="rotate(-90 5 50)">Percentage of GDP</text>
    <line x1="14" y1="73" x2="198" y2="73" stroke="#999" stroke-width=".4"/>
    <g transform="translate(15 5) scale(.82 .68)">
      <g fill="#111">
        <rect x="2" y="97.5" width="3" height="2.5"/><rect x="12" y="97.5" width="3" height="2.5"/><rect x="22" y="90" width="3" height="10"/><rect x="32" y="85" width="3" height="15"/><rect x="42" y="80" width="3" height="20"/><rect x="52" y="77" width="3" height="23"/><rect x="62" y="75" width="3" height="25"/><rect x="72" y="70" width="3" height="30"/><rect x="82" y="65" width="3" height="35"/><rect x="92" y="60" width="3" height="40"/><rect x="102" y="60" width="3" height="40"/><rect x="112" y="55" width="3" height="45"/><rect x="122" y="55" width="3" height="45"/><rect x="132" y="55" width="3" height="45"/><rect x="142" y="50" width="3" height="50"/><rect x="152" y="40" width="3" height="60"/><rect x="162" y="40" width="3" height="60"/><rect x="172" y="35" width="3" height="65"/><rect x="182" y="30" width="3" height="70"/><rect x="192" y="15" width="3" height="85"/><rect x="202" y="10" width="3" height="90"/>
      </g>
      <g fill="#c8c8c8">
        <rect x="5.5" y="85" width="3" height="15"/><rect x="15.5" y="97.5" width="3" height="2.5"/><rect x="25.5" y="97.5" width="3" height="2.5"/><rect x="35.5" y="95" width="3" height="5"/><rect x="45.5" y="85" width="3" height="15"/><rect x="55.5" y="95" width="3" height="5"/><rect x="65.5" y="90" width="3" height="10"/><rect x="75.5" y="80" width="3" height="20"/><rect x="85.5" y="67" width="3" height="33"/><rect x="95.5" y="60" width="3" height="40"/><rect x="105.5" y="40" width="3" height="60"/><rect x="115.5" y="75" width="3" height="25"/><rect x="125.5" y="97.5" width="3" height="2.5"/><rect x="135.5" y="87" width="3" height="13"/><rect x="145.5" y="80" width="3" height="20"/><rect x="155.5" y="95" width="3" height="5"/><rect x="165.5" y="60" width="3" height="40"/><rect x="175.5" y="85" width="3" height="15"/><rect x="185.5" y="90" width="3" height="10"/><rect x="195.5" y="60" width="3" height="40"/><rect x="205.5" y="60" width="3" height="40"/>
      </g>
    </g>
    <g font-size="2.3" fill="#444" text-anchor="end">
      <text transform="translate(18 76) rotate(-70)">Poland</text><text transform="translate(26.2 76) rotate(-70)">Portugal</text><text transform="translate(34.4 76) rotate(-70)">Korea</text><text transform="translate(42.6 76) rotate(-70)">Hungary</text><text transform="translate(50.8 76) rotate(-70)">Sweden</text><text transform="translate(59 76) rotate(-70)">Slovenia</text><text transform="translate(67.2 76) rotate(-70)">Spain</text><text transform="translate(75.4 76) rotate(-70)">Austria</text><text transform="translate(83.6 76) rotate(-70)">New Zealand</text><text transform="translate(91.8 76) rotate(-70)">Denmark</text><text transform="translate(100 76) rotate(-70)">Germany</text><text transform="translate(108.2 76) rotate(-70)">Finland</text><text transform="translate(116.4 76) rotate(-70)">France</text><text transform="translate(124.6 76) rotate(-70)">Luxembourg</text><text transform="translate(132.8 76) rotate(-70)">United States</text><text transform="translate(141 76) rotate(-70)">Belgium</text><text transform="translate(149.2 76) rotate(-70)">Japan</text><text transform="translate(157.4 76) rotate(-70)">Canada</text><text transform="translate(165.6 76) rotate(-70)">Norway</text><text transform="translate(173.8 76) rotate(-70)">Iceland</text><text transform="translate(182 76) rotate(-70)">Switzerland</text>
    </g>
    <rect x="26" y="98" width="3" height="3" fill="#111"/><text x="31" y="100.8" font-size="2.6" fill="var(--purple)">Expenditure on institutions (% of GDP)</text>
    <rect x="108" y="98" width="3" height="3" fill="#c8c8c8"/><text x="113" y="100.8" font-size="2.6" fill="var(--purple)">Expenditure on home care (% of GDP)</text>
  </svg>
  <p class="note" style="left:55px;top:146px;width:205px">Source: OECD Health Data, 2010. "Help Wanted? Providing and Paying for Long-Term Care," 2011.<br>Note: Home care includes day care spending. Data for some countries refer to earlier years.</p>
  <div class="brand-chip"><i></i>KESTREL LANE NURSING</div>
  <div class="page-no">04</div>
</section>

<!-- 05 Drivers list -->
<section class="slide col-l row3">
  <svg class="diag-panel" width="309" height="174" viewBox="0 0 309 174"><polygon points="226,0 309,0 309,174 193,174" fill="var(--purple)"/></svg>
  <h2 class="left-title">Key Industry <span class="accent">Drivers</span></h2>
  <div class="rule" style="left:21px;top:32px;width:25px"></div>
  <div class="list-item" style="top:47px"><span class="num">01</span><p>Health Care in Canada (public) was $331bn in 2022.<br>Only 3.8% of that, ($12.5bn) was for home and community care</p></div>
  <div class="list-item" style="top:75px"><span class="num">02</span><p>Private care represents about 25% of the total, suggesting<br>that home care provider industry in 2022 was about $16bn</p></div>
  <div class="list-item" style="top:104px"><span class="num">03</span><p>There were 4,295 businesses in this category, with the vast<br>majority doing $1-3m in annual revenue (owner operated)</p></div>
  <div class="list-item" style="top:132px;width:180px"><span class="num">04</span><p>Hearthway Care was the top company by revenue with about $440.3m<br>in this area (home health care), representing about 2.6% of the total</p></div>
  <div class="photo" style="left:191px;top:41px;width:84px;height:104px;background:linear-gradient(170deg,#efe9e2,#d8cbbd 60%,#6fa7c9);border:1px solid #fff" role="img" aria-label="Photo of a nurse in a white coat caring for a smiling older woman seated in a chair"></div>
  <div class="brand-chip"><i></i>KESTREL LANE NURSING</div>
  <div class="page-no">05</div>
</section>

<!-- 06 Consolidation -->
<section class="slide col-r row3">
  <h2 class="center-title" style="top:18px;font-size:8.4px">CATEGORY CONSOLIDATION IS COMING TO <span class="accent">HOME CARE</span></h2>
  <div class="rule" style="left:142px;top:31px;width:25px"></div>
  <div class="callout">By 2030, the $32bn Home Health Care sector will have 3 players delivering 75 % of the care – a dominant player with about 50%, a second with 20% and a third with 5% Hundreds of others will split the remaining and be $10-20m companies</div>
  <div class="small-list" style="top:100px"><span class="num">01</span>8.3% CAGR next 7 years</div>
  <div class="small-list" style="top:117px"><span class="num">02</span>Increased Regulation</div>
  <div class="small-list" style="top:134px"><span class="num">03</span>4,295 companies will collapse to 200-300</div>
  <div class="abs" style="left:154px;top:92px;width:1px;height:58px;background:var(--purple)"></div>
  <svg class="abs" style="left:170px;top:92px" width="112" height="63" viewBox="0 0 112 63" font-family="Open Sans, sans-serif">
    <rect x=".5" y=".5" width="111" height="62" fill="#fff" stroke="#e3e3e3" stroke-width=".5"/>
    <text x="10" y="5" font-size="3" fill="#777">Car Companies over time</text>
    <line x1="10" y1="52" x2="105" y2="52" stroke="#bbb" stroke-width=".4"/>
    <polyline points="12,50 20,40 27,10 33,30 40,50 55,55 75,56 100,56" fill="none" stroke="#3b6fd6" stroke-width=".7"/>
    <rect x="2" y="8" width="14" height="11" fill="#d6d6d6" role="img" aria-label="Small photo of an early motor car"/>
    <rect x="18" y="22" width="14" height="9" fill="#cfc3b8" role="img" aria-label="Small photo of a vintage car"/>
    <rect x="40" y="14" width="22" height="15" fill="#d3d3d3" role="img" aria-label="Small photo of an antique automobile"/>
    <rect x="12" y="33" width="18" height="15" fill="#c9c9c9" role="img" aria-label="Small photo of an antique automobile"/>
    <rect x="84" y="42" width="20" height="10" fill="#d8b9a6" role="img" aria-label="Small photo of a modern station wagon"/>
    <g font-size="1.8" fill="#777"><text x="12" y="56">1900</text><text x="32" y="56">1925</text><text x="52" y="56">1950</text><text x="72" y="56">1975</text><text x="92" y="56">2000</text><text x="56" y="60">Year</text></g>
  </svg>
  <div class="brand-chip"><i></i>KESTREL LANE NURSING</div>
  <div class="page-no">06</div>
</section>

<!-- 07 Denmark -->
<section class="slide col-l row4">
  <svg class="diag-panel" width="309" height="174" viewBox="0 0 309 174"><polygon points="226,0 309,0 309,174 193,174" fill="var(--purple)"/></svg>
  <h2 class="left-title" style="top:15px">Around the World: <span class="accent">Denmark</span></h2>
  <div class="rule" style="left:21px;top:34px;width:25px"></div>
  <div class="list-item" style="top:48px"><span class="num">01</span><p>Senior Friendly system with principles of self-reliance,<br>dignity and self-respect, integrated into the community</p></div>
  <div class="list-item" style="top:74px"><span class="num">02</span><p>National strategy to maintain people in their homes. In the<br>1980's legislated against the building of any new LTC homes</p></div>
  <div class="list-item" style="top:101px"><span class="num">03</span><p>Patient outcomes tracked, with funded nursing and caregiving<br>under universal health insurance</p></div>
  <div class="list-item" style="top:127px"><span class="num">04</span><p>Best outcomes and satisfaction levels of any<br>OECD country</p></div>
  <div class="photo" style="left:192px;top:37px;width:75px;height:102px;background:var(--map-red)" role="img" aria-label="White map of Denmark on a red square"></div>
  <div class="brand-chip"><i></i>KESTREL LANE NURSING</div>
  <div class="page-no">07</div>
</section>

<!-- 08 Problem -->
<section class="slide col-r row4" style="background:var(--purple)">
  <svg class="diag-panel" width="309" height="174" viewBox="0 0 309 174"><polygon points="309,0 309,174 30,174" fill="var(--green)"/></svg>
  <h2 class="abs split-title" style="left:29px;top:42px">Show Us A Problem</h2>
  <h2 class="abs split-title" style="right:13px;top:122px">We Didn’t Know We Had</h2>
  <div class="brand-chip"><i></i>KESTREL LANE NURSING</div>
  <div class="page-no">08</div>
</section>

</body>
</html>
```